Coffee and fruit juice

We are a malaysian restaurant that also serves aussie coffee and breakfast from 7am to 11am. After 11am we serve malaysian food but we also have a salad and sandwhich bar for people to choose from. We need a poster to hang outside our door to let people know that we are now also serving aussie coffee and breakfast as well as our usual malaysian cuisine.

Target Market(s)

Office location

Industry/Entity Type

Restaurant

Font styles to use
Decorative
Script

Requirements
Must have
• images and word
Nice to have
• something bold to attract people's attention

```html
<!DOCTYPE html>
<html lang="en">
<head>
<meta charset="utf-8">
<title>Now Open Poster</title>
<link rel="stylesheet" href="https://fonts.googleapis.com/css2?family=Oswald:wght@700&family=Arimo:wght@700&family=Yellowtail&family=Tinos:ital,wght@1,700&family=Poppins:wght@400&display=swap">
<style>
  :root {
    --page-bg: #e9e8e4;
    --olive: #4f6a1f;
    --olive-dark: #3b5417;
    --olive-light: #6c7f2c;
    --banner-white: #ffffff;
    --headline: #581c1c;
    --accent-yellow: #f2e400;
    --text-white: #ffffff;
  }
  * { margin: 0; padding: 0; box-sizing: border-box; }
  html, body {
    width: 1200px; height: 978px; overflow: hidden;
    background: var(--page-bg);
  }
  .poster {
    position: absolute; left: 308px; top: 39px;
    width: 584px; height: 900px;
    background: var(--olive);
    overflow: hidden;
  }
  .poster-shapes { position: absolute; inset: 0; }
  .headline {
    position: absolute; left: 0; width: 584px; top: 44px;
    text-align: center;
    font-family: "Oswald", "Arial Narrow", sans-serif;
    font-weight: 700; font-size: 104px; line-height: 1;
    letter-spacing: 6px; color: var(--headline);
    transform: rotate(-1.2deg);
  }
  .serving-now {
    position: absolute; left: 0; width: 584px; top: 652px;
    text-align: center;
    font-family: "Poppins", sans-serif; font-size: 30px;
    letter-spacing: 9px; color: var(--accent-yellow); line-height: 1;
  }
  .serving-script {
    position: absolute; left: 0; width: 584px; top: 682px;
    text-align: center;
    font-family: "Yellowtail", cursive; font-size: 42px;
    color: var(--accent-yellow); line-height: 1;
  }
  .offer {
    position: absolute; top: 760px; width: 280px;
    text-align: center; color: var(--text-white);
    font-family: "Arimo", Arial, sans-serif; font-weight: 700;
    line-height: 1;
  }
  .offer-breakfast { left: 14px; }
  .offer-lunch { left: 304px; }
  .offer-line-sm { font-size: 28px; }
  .offer-line-lg { font-size: 43px; margin-top: 2px; }
  .offer-line-md { font-size: 40px; }
  .offer-line-xs { font-size: 23px; margin-top: 2px; }
  .offer-hours {
    margin-top: 14px;
    font-family: "Tinos", "Times New Roman", serif;
    font-style: italic; font-weight: 700; font-size: 21px;
    color: var(--accent-yellow);
  }
</style>
</head>
<body>
  <main class="poster">
    <svg class="poster-shapes" width="584" height="900" viewBox="0 0 584 900">
      <defs>
        <linearGradient id="footer-green" x1="0" y1="0" x2="1" y2="1">
          <stop offset="0" stop-color="var(--olive-dark)"/>
          <stop offset="1" stop-color="var(--olive-light)"/>
        </linearGradient>
        <linearGradient id="main-dish" x1="0" y1="0" x2="1" y2="1">
          <stop offset="0" stop-color="#efe9dc"/>
          <stop offset="0.5" stop-color="#c98a45"/>
          <stop offset="1" stop-color="#6b3416"/>
        </linearGradient>
        <linearGradient id="tile-sandwich" x1="0" y1="0" x2="0" y2="1">
          <stop offset="0" stop-color="#d9a15a"/><stop offset="1" stop-color="#8fa84a"/>
        </linearGradient>
        <linearGradient id="tile-coffee" x1="0" y1="0" x2="0" y2="1">
          <stop offset="0" stop-color="#6e2a1a"/><stop offset="1" stop-color="#c9b49a"/>
        </linearGradient>
        <linearGradient id="tile-juice" x1="0" y1="0" x2="0" y2="1">
          <stop offset="0" stop-color="#f7f1e6"/><stop offset="1" stop-color="#f29a1c"/>
        </linearGradient>
        <linearGradient id="tile-salad" x1="0" y1="0" x2="0" y2="1">
          <stop offset="0" stop-color="#7fb23c"/><stop offset="1" stop-color="#c0642a"/>
        </linearGradient>
      </defs>
      <rect class="footer-panel" x="0" y="0" width="584" height="900" fill="url(#footer-green)"/>
      <rect class="top-band" x="0" y="0" width="584" height="24" fill="var(--olive)"/>
      <polygon class="headline-banner" points="0,24 584,24 584,165 0,183" fill="var(--banner-white)"/>
      <polygon class="photo-strip-frame" points="0,470 584,428 584,620 0,662" fill="#ffffff"/>
      <polygon class="main-dish-photo" role="img" aria-label="Photo of a Malaysian rice plate with rendang, fried chicken, egg and cucumber"
               points="4,183 584,165 584,432 4,474" fill="url(#main-dish)"/>
      <polygon class="tile-photo" role="img" aria-label="Photo of a sandwich" points="4,477 124,468 124,646 4,655" fill="url(#tile-sandwich)"/>
      <polygon class="tile-photo" role="img" aria-label="Photo of a latte with latte art" points="127,468 284,457 284,635 127,646" fill="url(#tile-coffee)"/>
      <polygon class="tile-photo" role="img" aria-label="Photo of glasses of fruit juice with orange slices" points="287,456 441,445 441,623 287,634" fill="url(#tile-juice)"/>
      <polygon class="tile-photo" role="img" aria-label="Photo of a fresh salad" points="444,445 584,435 584,613 444,623" fill="url(#tile-salad)"/>
    </svg>

    <h1 class="headline">NOW OPEN!</h1>

    <p class="serving-now">NOW</p>
    <p class="serving-script">Serving...</p>

    <section class="offer offer-breakfast">
      <p class="offer-line-sm">AUSSIE COFFEE &amp;</p>
      <p class="offer-line-lg">BREAKFAST</p>
      <p class="offer-hours">from 7am to 11am</p>
    </section>

    <section class="offer offer-lunch">
      <p class="offer-line-md">SALAD &amp;</p>
      <p class="offer-line-xs">SANDWHICH BAR</p>
      <p class="offer-hours">After 11am available</p>
    </section>
  </main>
</body>
</html>
```